Harvest Gathering event flyer

I would like a church event flyer designed. The event is called "HARVEST GATHERING 2018". I am looking for a professional, yet catchy design that uses our brand colors and logo creatively while communicating key information of the event effectively.

1. The logo is attached in two color formats. The designer has the choice to use them as he/she want.

2. The location of the event is: Lindqvist Community Center, 482 Tamsworth Street, Portland, ME 04102
3. Time and date of event. The designer can organize and format the date and time as he/she pleases.
December 28th, 29th @ 7:00PM
December 30th @ 10:00AM
4. The topic of the event is "Tongues of fire". The designer is free to use this phrase as he/she pleases to create a good composition.
5. Speaker: Prophet Marcus Obuya
6. Contact information: contact@cedarbrookfellowship.org - Telephone number: 207 555 0148

7. I would also like the following three words on the flyer. These words describe the focus of the event: FIRE, REVIVAL, PROPHETIC

```html
<!DOCTYPE html>
<html lang="en">
<head>
<meta charset="utf-8">
<title>Harvest Gathering 2018 – Event Flyer</title>
<link rel="stylesheet" href="https://fonts.googleapis.com/css2?family=Archivo+Black&family=Montserrat:wght@500;600;700;800&family=Oswald:wght@600&display=swap">
<style>
  :root {
    --navy: #0d3a66;
    --navy-deep: #0a2f55;
    --orange: #f39319;
    --ink: #2a2a2a;
    --white: #ffffff;
    --page: #e6e2dd;
  }
  * { margin: 0; padding: 0; box-sizing: border-box; }
  html, body { width: 1200px; height: 1200px; overflow: hidden; background: var(--page); }
  .flyer {
    position: absolute; left: 190px; top: 20px;
    width: 820px; height: 1160px;
    background: var(--white); overflow: hidden;
    font-family: "Montserrat", sans-serif;
    box-shadow: 0 6px 24px rgba(0,0,0,.18);
  }
  .hero {
    position: absolute; left: 0; top: 0; width: 820px; height: 410px;
    background: linear-gradient(180deg, #6e3b3c 0%, #c4552a 35%, #e98a2c 60%, #7a3a1e 82%, #1c1410 100%);
  }
  .brand {
    position: absolute; left: 40px; top: 60px; width: 230px; height: 140px;
    background: var(--navy);
    display: flex; align-items: center; justify-content: center; gap: 12px;
  }
  .brand-dot { width: 20px; height: 20px; border-radius: 50%; background: var(--orange); }
  .brand-name { color: var(--white); font-weight: 600; font-size: 40px; letter-spacing: 3px; }
  .info-panel {
    position: absolute; left: 0; top: 410px; width: 820px; height: 220px;
    background: var(--navy);
  }
  .title {
    position: absolute; left: 40px; top: 428px;
    font-family: "Archivo Black", sans-serif; font-size: 46px; line-height: 56px; color: var(--white);
    letter-spacing: .5px; white-space: nowrap;
  }
  .topic {
    position: absolute; left: 40px; top: 505px;
    color: var(--orange); font-weight: 700; font-size: 28px; letter-spacing: 1px;
  }
  .focus {
    position: absolute; left: 40px; top: 560px; display: flex; gap: 28px;
    list-style: none;
    color: var(--white); font-weight: 700; font-size: 20px; letter-spacing: 1px;
  }
  .focus-item { display: flex; align-items: center; gap: 10px; }
  .focus-item svg { width: 22px; height: 22px; }
  .speaker-band {
    position: absolute; left: 0; top: 630px; width: 820px; height: 50px;
    background: var(--orange);
  }
  .speaker {
    position: absolute; left: 40px; top: 642px;
    color: var(--white); font-weight: 600; font-size: 22px; letter-spacing: 1px;
  }
  .speaker-photo {
    position: absolute; left: 540px; top: 498px; width: 280px; height: 532px;
    background: linear-gradient(180deg, #7a5a48 0%, #3b2c26 40%, #1e1e22 70%, #8aa6c4 100%);
  }
  .schedule { position: absolute; left: 40px; top: 710px; color: var(--ink); font-weight: 800; }
  .schedule p { font-size: 37px; line-height: 48px; white-space: nowrap; }
  .schedule .gap { margin-top: 18px; }
  .venue { position: absolute; left: 40px; top: 930px; }
  .venue-name { font-family: "Oswald", sans-serif; color: var(--orange); font-size: 32px; line-height: 40px; }
  .venue-address { color: var(--ink); font-weight: 600; font-size: 20px; }
  .footer { position: absolute; left: 0; top: 1030px; width: 820px; height: 130px; }
  .phone {
    position: absolute; left: 40px; top: 1090px; display: flex; align-items: center; gap: 18px;
    color: var(--white); font-weight: 600; font-size: 34px; letter-spacing: 1px;
  }
  .email {
    position: absolute; left: 500px; top: 1042px; display: flex; align-items: center; gap: 10px;
    color: var(--white); font-weight: 500; font-size: 16px;
  }
</style>
</head>
<body>
<main class="flyer">
  <div class="hero" role="img" aria-label="Sunset sky over a hill with a wooden cross draped in cloth"></div>

  <div class="brand">
    <span class="brand-dot"></span>
    <span class="brand-name">KAVRO</span>
  </div>

  <section class="info-panel"></section>
  <h1 class="title">HARVEST GATHERING 2018</h1>
  <p class="topic">TONGUES OF FIRE</p>
  <ul class="focus">
    <li class="focus-item">
      <svg viewBox="0 0 24 24"><path fill="#f39319" d="M12 2c1 4 6 6 6 12a6 6 0 0 1-12 0c0-3 2-5 3-7 0 2 1 3 2 3 0-3 0-6 1-8z"/></svg>FIRE
    </li>
    <li class="focus-item">
      <svg viewBox="0 0 24 24"><path fill="#f39319" d="M12 2l3 7 7 3-7 3-3 7-3-7-7-3 7-3z"/></svg>REVIVAL
    </li>
    <li class="focus-item">
      <svg viewBox="0 0 24 24"><path fill="#f39319" d="M4 8c3-1 5 1 8 4 3-3 5-5 8-4-1 6-4 11-8 12-4-1-7-6-8-12z"/></svg>PROPHETIC
    </li>
  </ul>

  <div class="speaker-band"></div>
  <p class="speaker">SPEAKER: Prophet Marcus Obuya</p>

  <div class="speaker-photo" role="img" aria-label="Portrait of the speaker in a dark blazer and light blue shirt"></div>

  <div class="schedule">
    <p>December 28th, 29th</p>
    <p>@ 7:00PM</p>
    <p class="gap">December 30th</p>
    <p>@ 10:00AM</p>
  </div>

  <div class="venue">
    <p class="venue-name">LINDQVIST COMMUNITY CENTER</p>
    <p class="venue-address">482 Tamsworth Street, Portland, ME 04102</p>
  </div>

  <svg class="footer" viewBox="0 0 820 130" aria-hidden="true">
    <polygon points="440,0 820,0 820,45 480,45" fill="#f39319"/>
    <polygon points="0,45 820,45 820,130 0,130" fill="#0d3a66"/>
    <polygon points="440,0 480,45 0,45 0,45" fill="#0d3a66"/>
    <polygon points="480,45 820,45 820,52 486,52" fill="#ffffff"/>
  </svg>

  <div class="phone">
    <svg width="34" height="34" viewBox="0 0 24 24"><path fill="#f39319" d="M6.6 10.8a15 15 0 0 0 6.6 6.6l2.2-2.2c.3-.3.7-.4 1-.2 1.1.4 2.3.6 3.6.6.6 0 1 .4 1 1V20c0 .6-.4 1-1 1A17 17 0 0 1 3 4c0-.6.4-1 1-1h3.5c.6 0 1 .4 1 1 0 1.3.2 2.5.6 3.6.1.3 0 .7-.2 1z"/></svg>
    <span>207 555 0148</span>
  </div>

  <div class="email">
    <svg width="20" height="14" viewBox="0 0 20 14"><rect width="20" height="14" fill="#0d3a66"/><path d="M0 0l10 8 10-8" fill="none" stroke="#f39319" stroke-width="1.5"/></svg>
    <span>contact@cedarbrookfellowship.org</span>
  </div>
</main>
</body>
</html>
```